Flyer/Poster design required for volunteer activities

We need a STRIKING A4 Poster/Flyer advertising our conservation volunteer program activities which are currently happening in the area. This poster is to advertise the program once people have arrived on the island or to locals. The program covers 5 months, May-September 2019 and is focused on conservation. I have attached the following:
- a flyer which was previously created (QMR Habitat Helpers 2019 sm)to advertise the program - would prefer it has a similar striking resemblance, but not essential
- A mock up document 'HHQMR On Island Poster_2019_v2' with text -Logos-Images

Target Market(s)

Everyone interested in Environmental Adventure/Hiking/Citizen Science

Industry/Entity Type

Tourism

Font styles to use
Sans Serif

Requirements
Must have
• -A travel conservation focus
• -Must use 'QMR-Background Image' as the background to the design
• -The info of where to get more information and the social media details must be prominent

```html
<!DOCTYPE html>
<html lang="en">
<head>
<meta charset="utf-8">
<title>QMR Habitat Helpers – Program 2019</title>
<link rel="stylesheet" href="https://fonts.googleapis.com/css2?family=Roboto+Condensed:wght@700;800&family=Open+Sans:wght@400;600;700&display=swap">
<style>
  :root{
    --navy:#21378a;
    --blue:#1b78c4;
    --yellow:#ffe01b;
    --green:#8cbf3f;
    --green-light:#a6cf52;
    --orange:#e9582b;
    --ink:#262a33;
    --panel:rgba(236,238,246,.78);
    --white:#ffffff;
  }
  *{box-sizing:border-box;margin:0;padding:0}
  html,body{width:964px;height:1200px;overflow:hidden;background:#ffffff}
  .poster{position:relative;width:964px;height:1200px;overflow:hidden;font-family:"Open Sans",sans-serif;color:var(--ink)}
  .poster-background{position:absolute;inset:0;
    background:
      radial-gradient(ellipse at 70% 42%, #6f8a88 0%, rgba(111,138,136,0) 30%),
      linear-gradient(180deg,#bcd0da 0%,#3d78a8 38%,#2f6596 58%,#5b7c6a 80%,#7c7a44 100%);}
  .poster-shapes{position:absolute;inset:0}
  .abs{position:absolute}

  .brand-mark{left:100px;top:68px;width:136px;height:136px;border-radius:50%;border:4px solid var(--navy);background:var(--white);
    display:flex;align-items:center;justify-content:center;font-family:"Roboto Condensed",sans-serif;font-weight:800;font-size:40px;color:var(--navy)}
  .title{left:263px;top:62px;font-family:"Roboto Condensed",sans-serif;font-weight:800;line-height:1;letter-spacing:.5px}
  .title .line-one{display:block;font-size:66px;color:var(--navy)}
  .title .line-two{display:block;font-size:47px;color:var(--blue);margin-top:6px}

  .tagline{left:72px;top:242px;font-family:"Roboto Condensed",sans-serif;font-weight:800;font-size:37px;line-height:1.05;color:var(--white);transform:rotate(-3deg);transform-origin:left bottom;white-space:nowrap}
  .join{right:110px;top:222px;text-align:right;font-family:"Open Sans",sans-serif;font-weight:700;font-size:18.5px;line-height:1.28;color:var(--white)}
  .date-ribbon{left:365px;top:304px;width:305px;height:44px;background:var(--orange);border-radius:6px;transform:rotate(-12deg);
    display:flex;align-items:center;justify-content:center;font-family:"Roboto Condensed",sans-serif;font-weight:800;font-size:29px;color:var(--white);box-shadow:2px 4px 6px rgba(0,0,0,.3)}

  .month{top:392px;width:192px;height:516px;background:var(--panel);border:2px solid var(--yellow);padding:8px 8px 0}
  .month-title{font-family:"Roboto Condensed",sans-serif;font-weight:800;font-size:29px;color:var(--navy);text-align:center;line-height:1}
  .feature-label{text-align:center;font-size:14px;margin-top:4px;line-height:1.2}
  .feature-dates{text-align:center;font-size:15.5px;font-weight:600;line-height:1.25}
  .month-photo{height:122px;margin:7px 0 14px}
  .month-heading{font-family:"Open Sans",sans-serif;font-weight:700;font-size:17px;line-height:1.1;letter-spacing:-.2px;margin-bottom:5px}
  .activities{list-style:none}
  .activities li{position:relative;padding-left:17px;font-size:12.3px;line-height:1.3;margin-bottom:4px}
  .activities li::before{content:"";position:absolute;left:0;top:3px;width:10px;height:10px;border-radius:50%;background:var(--ink)}
  .activities li::after{content:"";position:absolute;left:3px;top:5px;width:4px;height:2px;border-left:1.6px solid #fff;border-bottom:1.6px solid #fff;transform:rotate(-45deg)}

  .september{left:87px;top:928px;width:788px;height:165px;background:var(--panel);border:2px solid var(--yellow)}
  .september .month-title{position:absolute;left:18px;top:20px;font-size:30px}
  .september .feature-label{position:absolute;left:18px;top:82px;text-align:left;font-size:14.5px}
  .september .feature-dates{position:absolute;left:18px;top:104px;font-size:17px}
  .september .month-photo{position:absolute;left:250px;top:12px;width:102px;height:146px;margin:0}
  .september-body{position:absolute;left:375px;top:10px;width:400px}
  .september-body .month-heading{font-weight:600;font-size:17.5px}
  .september-body .activities li{font-size:12.3px;margin-bottom:3px}

  .footer{left:0;width:964px;text-align:center;color:var(--white)}
  .footer-info{top:1111px;font-size:12.5px;letter-spacing:-.2px}
  .footer-follow{top:1130px;font-size:18px;letter-spacing:.3px}
  .footer-follow strong{font-weight:700;margin-left:14px}
</style>
</head>
<body>
<main class="poster">
  <div class="poster-background" role="img" aria-label="Aerial photograph of the island coastline with blue lagoon, green hills and distant peaks"></div>

  <svg class="poster-shapes" viewBox="0 0 964 1200" width="964" height="1200" aria-hidden="true">
    <path d="M0 0 H964 V215 Q760 196 560 194 Q300 194 0 210 Z" fill="#ffffff"/>
    <path d="M40 206 Q300 190 560 190 Q780 192 930 205 L930 390 Q780 382 600 366 Q420 352 250 346 Q130 342 40 338 Z" fill="var(--green)"/>
    <path d="M600 250 Q700 214 930 205 L930 390 Q780 384 640 370 Q580 310 600 250 Z" fill="var(--green-light)"/>
    <path d="M48 42 Q300 24 480 36 Q700 50 918 30 Q928 300 920 560 Q914 860 926 1160 Q640 1180 480 1168 Q260 1154 52 1174 Q60 900 50 600 Q40 300 48 42 Z"
          fill="none" stroke="var(--yellow)" stroke-width="17" stroke-linejoin="round"/>
  </svg>

  <div class="abs brand-mark">QMR</div>
  <h1 class="abs title"><span class="line-one">QUARRY MOSS REEF</span><span class="line-two">HABITAT HELPERS</span></h1>

  <p class="abs tagline">BE INVOLVED IN<br>PROTECTING PARADISE</p>
  <p class="abs join">JOIN THE QMR<br>HABITAT<br>HELPERS<br>PROGRAM 2019</p>
  <p class="abs date-ribbon">May - September 2019</p>

  <section class="abs month" style="left:87px">
    <h2 class="month-title">MAY 2019</h2>
    <p class="feature-label">Feature Week:</p>
    <p class="feature-dates">9th – 26th May</p>
    <div class="month-photo" role="img" aria-label="Photo of a grey seabird resting among green leaves" style="background:linear-gradient(135deg,#3f5a34,#9a948a 55%,#6c6a62)"></div>
    <h3 class="month-heading">BIRDS OF QUARRY MOSS REEF</h3>
    <ul class="activities">
      <li>Ocean bird watching boat trips</li>
      <li>Guided tours of Woodhen and Currawong quarters</li>
      <li>Weekly lectures at the Quarry Moss Reef Museum</li>
      <li>Weekly screenings of documentaries on Bird and Island Conservation projects</li>
      <li>Self guided land bird survey tours</li>
    </ul>
  </section>

  <section class="abs month" style="left:285px">
    <h2 class="month-title">JUNE 2019</h2>
    <p class="feature-label">Feature Week:</p>
    <p class="feature-dates">3rd- 9th June</p>
    <div class="month-photo" role="img" aria-label="Photo of a snorkeller recording notes on a slate underwater" style="background:linear-gradient(180deg,#1d6fa8,#3fa0cf 60%,#8fc4d6)"></div>
    <h3 class="month-heading">QUARRY MOSS REEF MARINE PARK</h3>
    <ul class="activities">
      <li>Marine pest monitoring with marine park staff</li>
      <li>Marine plastic &amp; debris clean up activities</li>
      <li>Screenings of marine conservation documentaries at the museum</li>
      <li>Weekly lectures on Marine Life at the Quarry Moss Reef Museum</li>
      <li>Marine Activities with local operators</li>
    </ul>
  </section>

  <section class="abs month" style="left:483px">
    <h2 class="month-title">JULY 2019</h2>
    <p class="feature-label">Feature Week:</p>
    <p class="feature-dates">21st - 28th July</p>
    <div class="month-photo" role="img" aria-label="Photo of a large dark stick insect resting on open hands" style="background:linear-gradient(135deg,#d8d2cc,#a89888 50%,#e6e2de)"></div>
    <h3 class="month-heading">INVASIVE SPECIES</h3>
    <ul class="activities">
      <li>Guided walks to learn about the weed eradication program</li>
      <li>Weekly lectures on plants of Quarry Moss Reef</li>
      <li>Weekly screenings of documentaries on plant and island conservation projects</li>
      <li>Guided walks to Mount Harrow</li>
      <li>Local tour guides include commentaries on island plants</li>
    </ul>
  </section>

  <section class="abs month" style="left:683px">
    <h2 class="month-title">AUGUST 2019</h2>
    <p class="feature-label">Feature Week:</p>
    <p class="feature-dates">11th-19th August</p>
    <div class="month-photo" role="img" aria-label="Photo of a hiker on a forest trail among palms" style="background:linear-gradient(135deg,#2f4a24,#7a8f4a 50%,#3d5a2c)"></div>
    <h3 class="month-heading">AMAZING INVERTEBRATES</h3>
    <ul class="activities">
      <li>Guided night walks to learn about the island's invertebrates</li>
      <li>Weekly viewing and presentation of the Quarry Moss Reef Phasmid</li>
      <li>Weekly lectures on invertebrates of Quarry Moss Reef at the museum</li>
      <li>Weekly screenings of documentaries on island conservation projects</li>
    </ul>
  </section>

  <section class="abs september">
    <h2 class="month-title">SEPTEMBER 2019</h2>
    <p class="feature-label">Feature Week:</p>
    <p class="feature-dates">1st-8th September</p>
    <div class="month-photo" role="img" aria-label="Photo of a walker on a hilltop lookout above the lagoon" style="background:linear-gradient(180deg,#a9c6df,#e6eef2 35%,#3b82ad 60%,#4d6a3a)"></div>
    <div class="september-body">
      <h3 class="month-heading">PROTECTING PARADISE</h3>
      <ul class="activities">
        <li>Observational snorkel surveys with Marine Ecologists, to assess populations of McCulloch's Anemonefish and other unique fish species</li>
        <li>Guided snorkel and glass bottom boat tour to assess coral health within the Quarry Moss Reef Marine Park</li>
        <li>Guided walks to learn about the island's conservation history</li>
      </ul>
    </div>
  </section>

  <p class="abs footer footer-info">See the QMR visitor centre for more information about the QMR Habitat Helpers program for 2019</p>
  <p class="abs footer footer-follow">FOLLOW US! <strong>www.hhqmr.org/follow&nbsp; photos@hhqmr</strong></p>
</main>
</body>
</html>
```